Single Page Production Company Site

Clean. Simple. Minimalist site with one page.

No portfolio, just some text to communicate a general overview of what the company does.

We work for a very select group of clients, creating strong brand personalities online. The site is specifically minimal and not communicating too much about what we do.. we have a variety of capabilities to work with clients and prefer to be broad with just a simple landing page as the point of contact for our brand.
Updates

Christmas holidays are coming up, maybe people need some time away from work with family and friends... We can keep working on this and I will provide feedback as quickly as possible, but I understand if designers have other commitments during the coming days. Thanks for your hard work!

Industry/Entity Type

Design Agency

Coding

Coded - Design and coding required

Number of Pages Required

1 page

Font styles to use
Sans Serif

Requirements
Must have
• Clean, bold text headlines.
Nice to have
• Unsure about any images used in the design, would like to see options with or without.

```html
<!DOCTYPE html>
<html lang="en">
<head>
<meta charset="utf-8">
<title>Cove Harbor Studio</title>
<link href="https://fonts.googleapis.com/css2?family=Ubuntu:wght@400;500;700&family=Raleway:wght@700&display=swap" rel="stylesheet">
<style>
:root{
  --cyan:#14b4e0;
  --teal:#0b98bb;
  --btn:#0a9ac0;
  --ink:#333;
  --grey-bg:#efefef;
  --grey-text:#8a8a8a;
  --navy:#030d2b;
  --navy-deep:#010a14;
  --white:#fff;
}
*{margin:0;padding:0;box-sizing:border-box}
html,body{width:1200px;height:3077px;overflow:hidden}
body{font-family:'Ubuntu',sans-serif;color:var(--ink);background:var(--grey-bg);position:relative}
.abs{position:absolute}
/* hero */
.hero{left:0;top:0;width:1200px;height:820px;overflow:hidden}
.hero-photo{position:absolute;inset:0;background:linear-gradient(135deg,#2a1360 0%,#4a2ba0 40%,#5b34bf 70%,#3a1d86 100%)}
.nav{left:0;top:0;width:1200px;height:58px;background:rgba(20,10,45,.55)}
.brand{left:52px;top:16px;font-size:21px;font-weight:500;color:var(--white)}
.nav-links{right:80px;top:14px;display:flex;align-items:center;gap:0}
.nav-links a{color:var(--white);text-decoration:none;font-size:19px;margin-right:46px}
.nav-links a.active{color:var(--cyan)}
.nav-cta{background:var(--btn);color:var(--white);font-size:14px;font-weight:700;padding:9px 14px;border-radius:3px;margin-left:-10px}
.hero-title{left:0;top:148px;width:1200px;text-align:center;font-size:50px;font-weight:700;color:var(--white);line-height:62px}
.hero-title span{color:var(--cyan)}
.feature{width:290px;text-align:center;color:var(--white)}
.feature svg{display:block;margin:0 auto 22px}
.feature h3{font-size:15.5px;color:var(--cyan);font-weight:700;margin-bottom:14px}
.feature p{font-size:15px;line-height:20px;text-align:justify;text-align-last:left}
.btn-outline{border:2px solid var(--cyan);color:var(--white);font-size:20px;border-radius:8px;text-align:center}
/* stats */
.stat{width:300px;text-align:center;font-family:'Raleway',sans-serif;font-size:17px;color:var(--grey-text)}
.stat svg{display:block;margin:14px auto 0}
.section-title{left:0;width:1200px;text-align:center;font-size:42px;font-weight:500;color:var(--ink)}
.section-title span{color:#3aa6c9}
.lead{left:270px;width:660px;text-align:center;font-size:15.5px;line-height:20px;color:#444}
.btn{background:var(--btn);color:var(--white);font-weight:700;font-size:16px;text-align:center;border-radius:8px}
.block-title{font-size:27px;font-weight:500;color:#222}
.body-text{font-size:15.5px;line-height:28px;color:#444;text-align:justify}
.photo{background:linear-gradient(180deg,#d9d9d9 0%,#4a4a55 55%,#1e2233 100%)}
.photo-light{background:linear-gradient(180deg,#cfc3b6 0%,#f3f3f3 45%,#dcdcdc 100%)}
.band{left:0;top:1727px;width:1200px;height:118px;background:var(--teal)}
.band-text{left:232px;top:40px;font-size:29px;font-weight:700;color:var(--white)}
.band-btn{left:828px;top:28px;width:235px;height:58px;border:2px solid var(--white);border-radius:4px;color:var(--white);font-size:20px;font-weight:700;text-align:center;line-height:54px}
/* footer */
.footer{left:0;top:2490px;width:1200px;height:535px;background:var(--navy);color:var(--white)}
.footer h4{font-size:20px;font-weight:700;margin-bottom:24px}
.footer h4 span{color:var(--cyan)}
.footer p{font-size:15.5px;line-height:20px;text-align:justify}
.quick li{list-style:none;font-size:16px;margin-bottom:20px}
.quick li.active{color:var(--cyan)}
.bottom{left:0;top:3025px;width:1200px;height:52px;background:var(--navy-deep)}
.copyright{left:50px;top:19px;font-size:12.5px;color:#cfd3da}
.social{right:60px;top:14px;display:flex;gap:26px}
.social span{width:22px;height:22px;border-radius:50%;background:var(--white);display:block}
</style>
</head>
<body>

<section class="abs hero">
  <div class="hero-photo" role="img" aria-label="Purple-toned photo of a desk with hands, laptop, coffee cup, papers and a calendar"></div>
  <header class="abs nav">
    <div class="abs brand">Cove Harbor Studio</div>
    <nav class="abs nav-links">
      <a class="active" href="#">home</a><a href="#">about</a><a href="#">services</a>
      <span class="nav-cta">CONTACT US</span>
    </nav>
  </header>
  <h1 class="abs hero-title">Creating <span>strong brand</span><br><span>personalities</span> online.</h1>

  <div class="abs feature" style="left:87px;top:390px">
    <svg width="66" height="78" viewBox="0 0 66 78" fill="none" stroke="#fff" stroke-width="3"><rect x="6" y="30" width="42" height="44" rx="4"/><path d="M48 40h6a8 8 0 0 1 0 16h-6"/><path d="M14 30V6M24 30V10M34 30V4M42 30V12"/></svg>
    <h3>DESIGN HAPPENS HERE</h3>
    <p>We are leading the way in design innovation for modern websites. Clean, functional, intuitive websites for progressive businesses.</p>
  </div>
  <div class="abs feature" style="left:453px;top:390px">
    <svg width="78" height="78" viewBox="0 0 78 78" fill="none" stroke="#fff" stroke-width="3"><path d="M70 6 36 44"/><path d="M28 46c-8 0-14 6-14 14 0 6-4 10-8 12 14 2 30-2 30-16z"/></svg>
    <h3>ART HAPPENS HERE</h3>
    <p>Building brands through design, we believe that contrast is everything. For industry leaders who set the pace and exceed expectations, we help give the company voice and soul.</p>
  </div>
  <div class="abs feature" style="left:822px;top:390px">
    <svg width="70" height="78" viewBox="0 0 70 78" fill="none" stroke="#fff" stroke-width="3"><path d="M20 74V58C10 52 6 42 8 32 10 18 22 10 36 10c14 0 26 10 26 24l6 12h-6v12H46v16"/><circle cx="36" cy="34" r="8"/></svg>
    <h3>IDEAS HAPPEN HERE</h3>
    <p>Clients look to us for unique, exceptional solutions to their technology issues. We bring creativity to the table and solve your business' problems with actionable solutions.</p>
  </div>
  <div class="abs btn-outline" style="left:500px;top:683px;width:197px;height:60px;line-height:56px">WORK WITH US</div>
</section>

<section>
  <div class="abs stat" style="left:15px;top:876px">15+ Years of experience
    <svg width="60" height="60" viewBox="0 0 60 60" fill="none" stroke="#555" stroke-width="2.5"><path d="M18 56V44C10 40 6 32 8 24 10 12 20 6 30 6c12 0 20 8 20 20l4 8h-4v10H38v12"/><circle cx="28" cy="26" r="7" fill="#f4b63a" stroke="#555"/></svg>
  </div>
  <div class="abs stat" style="left:450px;top:876px">670+ Projects completed
    <svg width="60" height="60" viewBox="0 0 60 60" fill="none" stroke="#555" stroke-width="2.5"><circle cx="34" cy="24" r="13" fill="#f4b63a"/><path d="M6 44h18l8-8M6 54h24l10-12"/></svg>
  </div>
  <div class="abs stat" style="left:873px;top:876px">100% Satisfied customers
    <svg width="60" height="60" viewBox="0 0 60 60" fill="none" stroke="#555" stroke-width="2.5"><path d="M12 4h36l-6 18H18z"/><circle cx="30" cy="38" r="16" fill="#f4b63a"/><path d="m30 30 3 6 6 1-4 4 1 6-6-3-6 3 1-6-4-4 6-1z"/></svg>
  </div>

  <h2 class="abs section-title" style="top:1024px">Let’s <span>work togeather</span></h2>
  <p class="abs lead" style="top:1108px">Cove Harbor Studio focuses on creating extraordinary online experiences for extraordinary clients. We’ll work with you to create the perfect online presence for your brand.</p>
  <div class="abs btn" style="left:514px;top:1202px;width:172px;height:54px;line-height:54px">LEARN MORE</div>

  <h3 class="abs block-title" style="left:166px;top:1396px">Our Goal</h3>
  <p class="abs body-text" style="left:166px;top:1464px;width:586px">Cove Harbor Studio brings your brand to life, online. We do it all when it comes to online commerce for retail stores, wholesalers and distributors. Taking your company online introduces a world of opportunity, as well as specific challenges associated with online trade. We’ll assist you in establishing a successful online presence and bringing your brand to a worldwide audience.</p>
  <div class="abs photo" style="left:893px;top:1300px;width:270px;height:427px;border-radius:120px 120px 0 0" role="img" aria-label="Photo of a smiling man in glasses and a dark blazer holding a coffee cup"></div>
</section>

<section class="abs band">
  <div class="abs band-text">Get your goals accomplished today.</div>
  <div class="abs band-btn">CONTACT US</div>
</section>

<section>
  <div class="abs photo-light" style="left:108px;top:1935px;width:302px;height:555px;border-radius:130px 130px 0 0" role="img" aria-label="Photo of a smiling man in a white t-shirt with arms crossed"></div>
  <h3 class="abs block-title" style="left:483px;top:2032px">We get you</h3>
  <div class="abs body-text" style="left:483px;top:2100px;width:587px">
    <p>Having a website isn’t enough. You need to show your customers you understand the socially connected online world we live in.</p>
    <p>We help you create designs that capture the personality of your business and project the image you want your customers to see. Maybe you’re a small company looking to sell yourself in the big leagues; maybe you’re a big company that wants to look approachable; either way, we can make it happen.</p>
    <p>You’ll come across looking professional, unique and strikingly hip all at the same time.</p>
  </div>
  <div class="abs btn" style="left:672px;top:2375px;width:174px;height:54px;line-height:54px">GET STARTED</div>
</section>

<footer class="abs footer">
  <div class="abs" style="left:50px;top:140px;width:336px">
    <h4>WHO’S <span>REID</span></h4>
    <p>Reid Halloway, owner of Cove Harbor Studio is not your typical principal. He’s worked internationally with both Marlow Press and Ardent House publications in photo production fortitles including Solstice and Gilded Hour. Originally from coastal Maine and an all-around New Englander, Reid can often be found sailing during the summer and skiing during winter. He believes that inspiration comes from experiencing the world, not from sitting in a cubicle. But no worries, his biggest fear is being offline, and is always within an arms reach of the Internett.</p>
  </div>
  <div class="abs" style="left:488px;top:140px;width:250px">
    <h4>QUICK MENU</h4>
    <ul class="quick">
      <li class="active">• HOME</li><li>• SERVICES</li><li>• ABOUT</li><li>• CONTACT</li>
    </ul>
  </div>
  <div class="abs" style="left:804px;top:140px;width:340px">
    <h4>ABOUT <span>COVE HARBOR STUDIO</span></h4>
    <p>We don’t work in a massive corporate office and we don’t have a mailroom. Not that there’s anything wrong with that, it’s just that we like knowing each other’s names, and encourage our clients to know ours. Our small staff has an advantage – our group works more efficiently, more cost-effectively and most importantly, flexible to each client’s unique needs. We deliver a range of services found at any agency, with the personal service you should expect.</p>
  </div>
</footer>

<div class="abs bottom">
  <div class="abs copyright">©All Rights Reserved by Cove Harbor Studio</div>
  <div class="abs social" aria-label="Social links"><span></span><span></span><span></span><span></span></div>
</div>

</body>
</html>
```